QuorintaFields background design

The task is to create a modern looking and very attractive background for the quorintaFields laboratory results reports + cover-page for the reports that matches the same design.

The background should be beautiful but also minimalistic enough not to interfere with the content inside the reports. If the background behind the content is too intensive then it is difficult to read the content. Our LOGO is blue and we have used blue-ish colors so far so perhaps one should try to keep blue at least as one of the colors. We have preferred to keep the design abstract/minimalistic rather than using photos.

Please look at the attached files, especially the file "Report with the current background" where you will see how the content is layed inside the reports. You will also see the current background that we would like to change. Then there is a file that contains the report pages without background that you could use to present the background.

```html
<!DOCTYPE html>
<html lang="en">
<head>
<meta charset="utf-8">
<title>QuorintaFields – Laboratory Test Results</title>
<link href="https://fonts.googleapis.com/css2?family=Open+Sans:wght@300;400;600;700&display=swap" rel="stylesheet">
<style>
  :root{
    --stage:#dcdcdc;
    --page-top:#dbeaf8;
    --page-mid:#f4f8fd;
    --brand:#2aa3df;
    --title:#3b9fd9;
    --ink:#3d3d3d;
    --muted:#555;
    --red:#e32b24;
    --orange:#f08a1c;
    --yellow:#f2d21a;
    --green:#3aa84a;
    --deco-a:#bcdcf3;
    --deco-b:#7fbde8;
  }
  *{box-sizing:border-box;margin:0;padding:0}
  html,body{width:1200px;height:956px;overflow:hidden}
  body{background:var(--stage);font-family:"Open Sans",sans-serif;color:var(--ink);position:relative}
  .page{
    position:absolute;left:285px;top:8px;width:630px;height:940px;overflow:hidden;
    background:linear-gradient(180deg,var(--page-top) 0%,var(--page-mid) 22%,#fbfdff 55%,#eef5fc 80%,#d6e8f7 100%);
  }
  .page__texture{position:absolute;left:80px;top:0;width:200px;height:110px;
    background:radial-gradient(ellipse at center,rgba(150,190,225,.35),rgba(150,190,225,0) 70%)}
  .page__art{position:absolute;left:0;bottom:0;width:630px;height:190px;
    background:
      radial-gradient(circle at 545px 120px,var(--deco-b) 0,rgba(127,189,232,0) 45px),
      radial-gradient(ellipse at 80px 150px,rgba(120,190,235,.7),rgba(120,190,235,0) 140px),
      linear-gradient(180deg,rgba(214,232,247,0),var(--deco-a));}
  .brand{position:absolute;right:52px;top:48px;display:flex;align-items:center;gap:8px}
  .brand__dot{width:26px;height:26px;border-radius:50%;background:var(--brand)}
  .brand__name{font-size:17px;font-weight:400;color:var(--brand)}
  .title{position:absolute;left:35px;top:130px;font-size:20px;font-weight:400;color:var(--title);letter-spacing:.2px}
  .results{position:absolute;left:35px;top:196px;width:562px;display:grid;
    grid-template-columns:252px 265px;column-gap:30px;grid-template-rows:204px 203px auto}
  .metric__head{display:flex;justify-content:space-between;align-items:baseline;font-size:11px;font-weight:700;color:#444}
  .metric__value{font-size:9.5px;font-weight:700}
  .metric__value sup{font-size:6px}
  .gauge{position:relative;height:34px}
  .gauge__pin{position:absolute;top:10px;width:12px;height:16px;margin-left:-6px}
  .gauge__bar{position:absolute;left:2px;right:2px;bottom:0;height:5px;border-radius:2px}
  .gauge__bar::before,.gauge__bar::after{content:"";position:absolute;top:0;width:1px;height:5px;background:#fff}
  .gauge__bar::before{left:33.3%}.gauge__bar::after{left:66.6%}
  .bar--range{background:linear-gradient(90deg,var(--red),var(--orange) 12%,var(--yellow) 24%,var(--green) 42%,var(--green) 60%,var(--yellow) 76%,var(--orange) 88%,var(--red))}
  .bar--rising{background:linear-gradient(90deg,var(--green),var(--green) 30%,var(--yellow) 55%,var(--orange) 78%,var(--red))}
  .bar--falling{background:linear-gradient(90deg,var(--red),var(--orange) 18%,var(--yellow) 38%,var(--green) 62%,var(--green))}
  .scale{display:flex;justify-content:space-between;font-size:8.5px;color:var(--muted);margin-top:5px;padding:0 3px}
  .scale__normal{margin-left:26px}
  .metric__text{margin-top:14px;font-size:8.7px;line-height:14.5px;text-align:justify;color:#4a4a4a}
</style>
</head>
<body>
  <main class="page">
    <div class="page__texture" role="img" aria-label="Faint molecular dot texture"></div>
    <div class="page__art" role="img" aria-label="Soft blue illustration of DNA strands and molecules"></div>

    <div class="brand"><span class="brand__dot"></span><span class="brand__name">QuorintaFields</span></div>
    <h1 class="title">LABORATORY TEST RESULTS</h1>

    <section class="results">
      <article class="metric">
        <div class="metric__head"><span>Glucose</span><span class="metric__value">78 mg/dl</span></div>
        <div class="gauge">
          <svg class="gauge__pin" style="left:50%" viewBox="0 0 12 16"><path d="M6 1a4.5 4.5 0 0 1 4.5 4.5C10.5 9 6 15 6 15S1.5 9 1.5 5.5A4.5 4.5 0 0 1 6 1z" fill="#fff" stroke="#666"/><circle cx="6" cy="5.5" r="1.6" fill="none" stroke="#666"/></svg>
          <div class="gauge__bar bar--range"></div>
        </div>
        <div class="scale"><span>low</span><span>normal 60-99</span><span>high</span></div>
        <p class="metric__text">Glucose is the main source of energy for the body. The danger of continuously high blood glucose is that sugar coats the red blood cells, causing them to become stiff and "sticky". These cells interfere with proper blood circulation and cause build-up on blood vessels. High blood sugar can lead to cardiovascular and kidney disease, blindness, or ulcers.</p>
      </article>

      <article class="metric">
        <div class="metric__head"><span>C-reactive protein</span><span class="metric__value">1.2 mg/l</span></div>
        <div class="gauge">
          <svg class="gauge__pin" style="left:7%" viewBox="0 0 12 16"><path d="M6 1a4.5 4.5 0 0 1 4.5 4.5C10.5 9 6 15 6 15S1.5 9 1.5 5.5A4.5 4.5 0 0 1 6 1z" fill="#fff" stroke="#666"/><circle cx="6" cy="5.5" r="1.6" fill="none" stroke="#666"/></svg>
          <div class="gauge__bar bar--rising"></div>
        </div>
        <div class="scale"><span>normal ≤5</span><span>high</span></div>
        <p class="metric__text">C-reactive protein (CRP) is a general inflammation marker. Any tissue injury or infection will raise the amount of CRP in the blood within a few hours. After the inflammation is gone, CRP goes down fast. Increased CRP levels not related to acute illness or infection have been linked to higher risk of heart disease.</p>
      </article>

      <article class="metric">
        <div class="metric__head"><span>Sodium</span><span class="metric__value">142 mmol/l</span></div>
        <div class="gauge">
          <svg class="gauge__pin" style="left:55%" viewBox="0 0 12 16"><path d="M6 1a4.5 4.5 0 0 1 4.5 4.5C10.5 9 6 15 6 15S1.5 9 1.5 5.5A4.5 4.5 0 0 1 6 1z" fill="#fff" stroke="#666"/><circle cx="6" cy="5.5" r="1.6" fill="none" stroke="#666"/></svg>
          <div class="gauge__bar bar--range"></div>
        </div>
        <div class="scale"><span>low</span><span>normal 136-146</span><span>high</span></div>
        <p class="metric__text">The amount of sodium is closely related to the amount of water in the body. Excess levels may occur in dehydration, excess sodium in your diet or several diseases. Low levels may occur in cases of heart failure, severe sweating, diarrhea or vomiting, poor nutrition or drinking too much water.</p>
      </article>

      <article class="metric">
        <div class="metric__head"><span>Potassium</span><span class="metric__value">5.2 mmol/l</span></div>
        <div class="gauge">
          <svg class="gauge__pin" style="left:70%" viewBox="0 0 12 16"><path d="M6 1a4.5 4.5 0 0 1 4.5 4.5C10.5 9 6 15 6 15S1.5 9 1.5 5.5A4.5 4.5 0 0 1 6 1z" fill="#fff" stroke="#666"/><circle cx="6" cy="5.5" r="1.6" fill="none" stroke="#666"/></svg>
          <div class="gauge__bar bar--range"></div>
        </div>
        <div class="scale"><span>low</span><span>normal 3.5-5.1</span><span>high</span></div>
        <p class="metric__text">Potassium helps nerves and muscles communicate. Dehydration, diarrhea, and excessive sweating are common causes of low potassium levels. Changes in potassium level alter the activity of nerves and muscles, especially the heart: low levels can lead to an irregular heartbeat and high levels cause decreased heart muscle activity.</p>
      </article>

      <article class="metric">
        <div class="metric__head"><span>Creatinine</span><span class="metric__value">1.1 mg/dl</span></div>
        <div class="gauge">
          <svg class="gauge__pin" style="left:61%" viewBox="0 0 12 16"><path d="M6 1a4.5 4.5 0 0 1 4.5 4.5C10.5 9 6 15 6 15S1.5 9 1.5 5.5A4.5 4.5 0 0 1 6 1z" fill="#fff" stroke="#666"/><circle cx="6" cy="5.5" r="1.6" fill="none" stroke="#666"/></svg>
          <div class="gauge__bar bar--range"></div>
        </div>
        <div class="scale"><span>low</span><span>normal 0.7-1.2</span><span>high</span></div>
        <p class="metric__text">Creatinine is critical for evaluating renal function. Your serum creatinine is a waste product that is formed when muscle cells break down in your blood. It is produced by muscles as it depends on muscle mass and protein intake. High levels could indicate kidney dysfunction while decreased levels may reflect low muscle mass.</p>
      </article>

      <article class="metric">
        <div class="metric__head"><span>EGFR</span><span class="metric__value">98 ml/min/1.73 m<sup>2</sup></span></div>
        <div class="gauge">
          <svg class="gauge__pin" style="left:81%" viewBox="0 0 12 16"><path d="M6 1a4.5 4.5 0 0 1 4.5 4.5C10.5 9 6 15 6 15S1.5 9 1.5 5.5A4.5 4.5 0 0 1 6 1z" fill="#fff" stroke="#666"/><circle cx="6" cy="5.5" r="1.6" fill="none" stroke="#666"/></svg>
          <div class="gauge__bar bar--falling"></div>
        </div>
        <div class="scale"><span>low</span><span>normal &gt;60</span></div>
        <p class="metric__text">An estimated glomerular filtration rate (eGFR) is calculated according to your creatinine level, age, sex and race. The eGFR is used to screen for and detect early kidney damage and to monitor kidney status. An eGFR below 60 mL/min suggests that some kidney damage has occurred.</p>
      </article>
    </section>
  </main>
</body>
</html>
```